Tillwave - New Payment App for Student

Till-wave - A Payment App for student to make payment, track own expenses and practice good dietary habits. The App theme is Fun and excitement.
Target User: Secondary Student aged 13-18
Look and Feel: Fun, excitement and simple.
Screen 1
Login to the app using thumbprints or password
Screen 2
Display the balance
Wallet balance >>> go to screen 3 to display transaction history
Gamification balance - points + badges >>> go to screen 3
Button to make payment
Screen 2-1
Allow them to do payment
Click “Pay”
Display QR code
scanning by merchant
Payment made
Notification received
The transaction history will be shown up
Screen 2-2
Allow them to top up (alternatively to parent Top-up using credit card)
Click “Top Up”
Display QR code
Pass the cash to merchant
scanning by merchant
Payment made
Notification received
The new balance will be shown up
Screen 3
Display more details on transaction history
Payment history + gamification history (gain/redeem points)
E.g. 14 Nov Canteen purchase $5.40
- Banana +30 points
- Milk +10 points
Screen 4 (play a game to earn point)
Introduce some trivial games (while waiting in line at cafeteria or school store) to gain some points
Crosswords
Puzzle
Screen 5 (Display achievements)
Leaderboard
Where the individual stands in the class
Where the class stands overall in school
Badges
Level
Achievements
For more, please go to our website http://www.tillwave.example/
Updates
Target Market(s)
Secondary School Student aged 13-18
Industry/Entity Type
Education
Logo Text
tillwave
Look and feel

```html
<!DOCTYPE html>
<html lang="en">
<head>
<meta charset="utf-8">
<title>Tillwave – Wallet Home</title>
<link rel="stylesheet" href="https://fonts.googleapis.com/css2?family=Nunito+Sans:wght@300;400;600;700&display=swap">
<style>
  :root {
    --page-bg: #e9ecef;
    --header-top: #6a4fc8;
    --header-bottom: #4a72cf;
    --wave: rgba(255,255,255,0.14);
    --points-green: #3fcf98;
    --section-grey: #f3f2f1;
    --text-dark: #3f4246;
    --text-mid: #6b6f74;
    --text-light: #a3a7ab;
    --divider: #e4e4e4;
    --avatar-grey: #e2e2e2;
    --fab-pink: #f23f6a;
    --white: #ffffff;
    --notify-red: #ff4b5c;
  }
  * { box-sizing: border-box; margin: 0; padding: 0; }
  html, body { width: 1200px; height: 1200px; overflow: hidden; }
  body {
    background: var(--page-bg);
    font-family: "Nunito Sans", "Helvetica Neue", Arial, sans-serif;
    color: var(--text-dark);
    position: relative;
  }
  .app-screen {
    position: absolute;
    left: 300px; top: 66px;
    width: 600px; height: 1067px;
    background: var(--white);
    overflow: hidden;
    border-radius: 8px;
    box-shadow: 0 20px 60px rgba(40,40,70,0.15);
  }
  .wallet-header {
    position: absolute; left: 0; top: 0; width: 600px; height: 460px;
    background: linear-gradient(170deg, var(--header-top) 0%, var(--header-bottom) 100%);
    color: var(--white);
  }
  .status-bar {
    position: absolute; left: 0; top: 0; width: 100%; height: 40px;
    display: flex; align-items: center; justify-content: space-between;
    padding: 0 18px; font-size: 15px; font-weight: 600;
  }
  .status-left, .status-right { display: flex; align-items: center; gap: 6px; }
  .status-time { position: absolute; left: 50%; transform: translateX(-50%); }
  .menu-button { position: absolute; left: 30px; top: 66px; width: 30px; height: 24px; }
  .current-label {
    position: absolute; top: 140px; width: 100%; text-align: center;
    font-size: 18px; letter-spacing: 1.5px; font-weight: 400; opacity: 0.75;
  }
  .balance {
    position: absolute; top: 180px; width: 100%;
    display: flex; justify-content: center; align-items: flex-start; gap: 8px;
    font-weight: 300;
  }
  .balance-currency { font-size: 28px; margin-top: 22px; }
  .balance-amount { font-size: 88px; line-height: 1; letter-spacing: -1px; }
  .balance-unit { font-size: 24px; margin-top: 12px; opacity: 0.9; }
  .points-pill {
    position: absolute; top: 312px; left: 200px;
    height: 56px; width: 220px; border-radius: 28px;
    background: var(--points-green);
    display: flex; align-items: center; padding-left: 78px;
    font-size: 20px; font-weight: 600;
  }
  .points-badge {
    position: absolute; left: 180px; top: 302px; width: 76px; height: 76px;
    border-radius: 50%; background: var(--white);
    display: flex; align-items: center; justify-content: center;
    box-shadow: 0 4px 10px rgba(0,0,0,0.12);
  }
  .header-waves { position: absolute; left: 0; bottom: 0; width: 600px; height: 110px; }
  .history-bar {
    position: absolute; left: 0; top: 460px; width: 600px; height: 110px;
    background: var(--section-grey);
  }
  .history-chevron { position: absolute; right: 30px; top: 22px; }
  .history-title { position: absolute; left: 34px; bottom: 22px; font-size: 22px; color: var(--text-mid); }
  .transaction-list { position: absolute; left: 0; top: 570px; width: 600px; list-style: none; }
  .transaction {
    position: relative; height: 140px; margin-left: 34px;
    border-bottom: 1px solid var(--divider);
  }
  .merchant-avatar {
    position: absolute; left: 0; top: 40px; width: 62px; height: 62px; border-radius: 50%;
    background: var(--avatar-grey); color: var(--text-light);
    display: flex; align-items: center; justify-content: center; font-size: 24px;
  }
  .merchant-avatar.is-cafe { background: #2e6b4f; color: var(--white); font-weight: 700; }
  .merchant-name { position: absolute; left: 90px; top: 36px; font-size: 19px; font-weight: 700; color: var(--text-dark); }
  .merchant-amount { position: absolute; left: 90px; top: 62px; font-size: 34px; font-weight: 300; color: var(--text-dark); }
  .transaction-time { position: absolute; right: 34px; top: 18px; font-size: 15px; color: var(--text-light); }
  .transaction-points { position: absolute; right: 34px; top: 42px; font-size: 24px; color: var(--points-green); font-weight: 400; }
  .pay-button {
    position: absolute; right: 28px; top: 830px; width: 76px; height: 76px; border-radius: 50%;
    background: var(--fab-pink); box-shadow: 0 6px 16px rgba(242,63,106,0.35);
    display: flex; align-items: center; justify-content: center;
  }
</style>
</head>
<body>
  <main class="app-screen">
    <section class="wallet-header">
      <div class="status-bar">
        <div class="status-left">
          <svg width="40" height="8" viewBox="0 0 40 8" aria-hidden="true">
            <circle cx="4" cy="4" r="3.2" fill="#fff"/><circle cx="12" cy="4" r="3.2" fill="#fff"/>
            <circle cx="20" cy="4" r="3.2" fill="#fff"/><circle cx="28" cy="4" r="2.8" fill="none" stroke="#fff"/>
            <circle cx="36" cy="4" r="2.8" fill="none" stroke="#fff"/>
          </svg>
          <span>ORBIT</span>
          <svg width="16" height="12" viewBox="0 0 16 12" aria-hidden="true"><path d="M1 4a10 10 0 0 1 14 0M3.5 6.5a6.5 6.5 0 0 1 9 0M6 9a3 3 0 0 1 4 0" stroke="#fff" stroke-width="1.6" fill="none"/></svg>
        </div>
        <span class="status-time">4:21 PM</span>
        <div class="status-right">
          <svg width="9" height="14" viewBox="0 0 9 14" aria-hidden="true"><path d="M1 4l7 6-3.5 3V1L8 4 1 10" stroke="#fff" stroke-width="1.3" fill="none"/></svg>
          <span>22%</span>
          <svg width="28" height="13" viewBox="0 0 28 13" aria-hidden="true"><rect x="0.5" y="0.5" width="24" height="12" rx="3" fill="none" stroke="#fff"/><rect x="2" y="2" width="6" height="9" rx="1" fill="#fff"/><rect x="25.5" y="4" width="2" height="5" rx="1" fill="#fff"/></svg>
        </div>
      </div>

      <svg class="menu-button" viewBox="0 0 30 24" aria-label="Menu">
        <path d="M2 6h18M2 13h18M2 20h18" stroke="#fff" stroke-width="2" stroke-linecap="round"/>
        <circle cx="24" cy="4" r="4" fill="var(--notify-red)"/>
      </svg>

      <p class="current-label">CURRENT BALANCE</p>
      <div class="balance">
        <span class="balance-currency">$</span>
        <span class="balance-amount">1,950</span>
        <span class="balance-unit">SG</span>
      </div>

      <div class="points-pill">12,220 points</div>
      <div class="points-badge">
        <svg width="34" height="30" viewBox="0 0 34 30" aria-hidden="true">
          <path d="M8 2h18l6 8-15 18L2 10z M2 10h30 M12 2l-3 8 8 18 8-18-3-8 M9 10l8-8 8 8" fill="none" stroke="#46b3c9" stroke-width="1.6" stroke-linejoin="round"/>
        </svg>
      </div>

      <svg class="header-waves" viewBox="0 0 600 110" preserveAspectRatio="none" aria-hidden="true">
        <path d="M0 90 C120 40 220 70 330 50 S520 10 600 30 V110 H0z" fill="var(--wave)"/>
        <path d="M0 100 C140 70 260 95 380 75 S540 50 600 60 V110 H0z" fill="var(--wave)"/>
      </svg>
    </section>

    <section class="history-bar">
      <svg class="history-chevron" width="14" height="24" viewBox="0 0 14 24" aria-label="See all"><path d="M2 2l10 10-10 10" stroke="#8a8d91" stroke-width="2" fill="none"/></svg>
      <h2 class="history-title">Transaction history</h2>
    </section>

    <ul class="transaction-list">
      <li class="transaction">
        <span class="merchant-avatar is-cafe">B</span>
        <span class="merchant-name">Brewhaus</span>
        <span class="merchant-amount">$12.87</span>
        <span class="transaction-time">4h ago</span>
        <span class="transaction-points">+60 pts</span>
      </li>
      <li class="transaction">
        <span class="merchant-avatar">S</span>
        <span class="merchant-name">School Canteen</span>
        <span class="merchant-amount">$10.76</span>
        <span class="transaction-time">12h ago</span>
        <span class="transaction-points">+45 pts</span>
      </li>
      <li class="transaction">
        <span class="merchant-avatar">A</span>
        <span class="merchant-name">Ante vestibulum</span>
        <span class="merchant-amount">$52</span>
        <span class="transaction-time">Yesterday</span>
        <span class="transaction-points">+85 pts</span>
      </li>
    </ul>

    <div class="pay-button" aria-label="Make a payment">
      <svg width="28" height="28" viewBox="0 0 28 28" aria-hidden="true"><path d="M14 4v20M4 14h20" stroke="#fff" stroke-width="2.4" stroke-linecap="round"/></svg>
    </div>
  </main>
</body>
</html>
```